Generator Control - Superyacht Power Management System

We need a graphic design for a Touch Screen interface to control generators on Superyachts. We have a layout of the control system worked out, but need nice graphics to go with it.
The graphics comes down to a 300x460px App that i replicate several times on my 15" touchscreen as required.
See attached images.
The interface is divided up into 4 sections:
• Section#1 - 4 rectangles for the control
• Section#2 - a vertical bar graph,
• Section#3 - a section to display custom information
• Section#4 - a circuit breaker symbol.
The dimensions in pixels must be as per the attached image.
SECTION#1:
The 4 control rectangles correspond to 4 control modes:
• STOP – colours based on RED
• RUN – colours based on ORANGE
• RUN ONLINE – colours based on GREEN
• AUTO – colours based on BLUE
• THE TEXT DOESN’T HAVE TO BE ON THE GRAPHICS, WE JUST NEED THE BACKGROUND FOR THE TEXT, I ADD THE TEXT LATER USING SOFTWARE.
Each control rectangle needs to have 3 clearly identifiable states:
• Active/Selected (this is the currently active mode)
• Not Active/Not Selected (this mode is available but not currently active)
• Unavailable (this mode is not available)
SECTION#2:
The vertical bar graph design only needs the outline/frame of the bar graph. The actual moving part can be left blank; I will add that in later using an animation.
SECTION#3:
Free to look good as you want. See attached image for reference.
Within section#3 (at the top) is a 40x240px subsection, and should simply by 2 states, green or 'background colour of section#3 '. (green for when the generator is running, blend with the rest of section#3 when it is not). There are about 10 different texts I add on top of that square using software, corresponding to the status of the generator (starting, deloading, synchronizing, etc.)
SECTION#4:
Graphical representation of an electrical switch. Can be in two positions: opened or closed. See attached image as reference.

Cheif Engineers /Captains on Superyachts

Graphic Design

• Must have the same graphics style as the uploaded file#2

```html
<!DOCTYPE html>
<html lang="en">
<head>
<meta charset="UTF-8">
<title>Generator Control</title>
<link href="https://fonts.googleapis.com/css2?family=Arimo:wght@400;700&display=swap" rel="stylesheet">
<style>
  :root{
    --bg:#15191d;
    --panel:#1c2126;
    --panel-edge:#3a424b;
    --field:#1a1f24;
    --field-edge:#55606c;
    --text:#e8edf2;
    --text-dim:#c9d0d8;
    --green-hi:#9be34a;
    --green:#5cc21e;
    --green-lo:#3a8f0f;
    --blue-hi:#38c4ff;
    --blue:#1596e0;
    --blue-lo:#0b5fa3;
    --grey-hi:#4a5058;
    --grey-lo:#2c3036;
    --muted:#6b7179;
    --red-hi:#ff4a3e;
    --red:#d8140f;
    --red-lo:#8e0705;
    --seg-off:#3a3f46;
  }
  *{box-sizing:border-box;margin:0;padding:0}
  html,body{width:783px;height:1200px;overflow:hidden;background:var(--bg)}
  body{position:relative;font-family:"Arimo",Arial,sans-serif;color:var(--text)}
  .abs{position:absolute}

  .breaker-housing{left:334px;top:31px;width:115px;height:157px;border-radius:8px;
    background:linear-gradient(#2a2f35,#1b1f23);border:2px solid #0e1114;box-shadow:0 0 0 2px #2e343a}
  .breaker-switch{left:347px;top:47px;width:89px;height:89px;border-radius:6px;
    background:linear-gradient(var(--red-hi),var(--red) 55%,var(--red-lo));
    box-shadow:inset 0 3px 4px rgba(255,255,255,.35),0 4px 8px rgba(0,0,0,.6)}
  .breaker-switch::after{content:"";position:absolute;left:42px;top:48px;width:4px;height:20px;background:#ffd1cc;border-radius:2px}
  .breaker-lead{left:390px;top:188px;width:3px;height:75px;background:#4b535c}

  .panel{background:var(--panel);border:2px solid var(--panel-edge);border-radius:10px;
    box-shadow:inset 0 0 0 2px #101316}
  .mode-panel{left:13px;top:269px;width:600px;height:389px}
  .info-panel{left:13px;top:663px;width:600px;height:525px}
  .power-panel{left:639px;top:269px;width:131px;height:919px}

  .mode-btn{width:274px;height:170px;border-radius:10px;display:flex;align-items:center;justify-content:center;
    text-align:center;font-size:30px;line-height:1.25;text-transform:uppercase}
  .mode-run-online{left:31px;top:287px;color:#1d3b06;font-weight:700;
    background:linear-gradient(var(--green-hi),var(--green) 50%,var(--green-lo));
    border:4px solid #f4f7f2;box-shadow:0 0 10px rgba(155,227,74,.45)}
  .mode-run{left:324px;top:287px;color:var(--muted)}
  .mode-stop{left:31px;top:475px;color:var(--muted)}
  .mode-idle{background:linear-gradient(var(--grey-hi),var(--grey-lo));border:3px solid #23272c}
  .mode-auto{left:324px;top:475px;color:#d9f3ff;
    background:linear-gradient(var(--blue-hi),var(--blue) 50%,var(--blue-lo));border:3px solid #0a3f6e}

  .status-banner{left:39px;top:679px;width:548px;height:99px;border-radius:9px;
    background:linear-gradient(#7fd835,var(--green) 55%,#48a416);
    display:flex;align-items:center;justify-content:center;font-size:44px;font-weight:700;color:#f4fbee}

  .readout{left:39px;width:177px;height:73px;border-radius:9px;background:var(--field);
    border:3px solid var(--field-edge);display:flex;align-items:center;justify-content:center;font-size:30px}
  .readout-label{left:232px;font-size:26px;line-height:1.05;color:var(--text-dim)}
  .electrical{left:412px;top:806px;width:175px;height:358px;border-radius:9px;background:var(--field);
    border:3px solid var(--field-edge);text-align:center;font-size:28px;line-height:1.2;padding-top:14px}
  .electrical .gap{height:30px}

  .load-pct{left:639px;top:304px;width:131px;text-align:center;font-size:28px;font-weight:700}
  .load-pct small{font-size:18px}
  .scale-label{left:650px;font-size:19px;color:var(--text-dim);transform:rotate(-90deg);transform-origin:center;width:40px;text-align:center}
  .tube{left:684px;top:358px;width:73px;height:726px;border-radius:30px;padding:14px 9px;
    background:linear-gradient(90deg,#15181b,#2c3137 50%,#15181b);border:3px solid #454d56;
    display:flex;flex-direction:column;gap:5px}
  .seg{flex:1;border-radius:8px;background:linear-gradient(90deg,#2a2e33,var(--seg-off) 50%,#2a2e33)}
  .seg.on{background:linear-gradient(90deg,#3c8f12,var(--green-hi) 50%,#3c8f12)}
  .tick{left:674px;width:8px;height:2px;background:#7d8690}
  .kw-value{left:639px;top:1110px;width:131px;text-align:center;font-size:30px;font-weight:700}
  .kw-unit{left:639px;top:1148px;width:131px;text-align:center;font-size:18px;font-weight:700}
</style>
</head>
<body>
  <div class="abs breaker-housing"></div>
  <div class="abs breaker-switch" role="img" aria-label="Circuit breaker, closed"></div>
  <div class="abs breaker-lead"></div>

  <div class="abs panel mode-panel"></div>
  <div class="abs mode-btn mode-run-online">Run<br>Online</div>
  <div class="abs mode-btn mode-idle mode-run">Run</div>
  <div class="abs mode-btn mode-idle mode-stop">Stop</div>
  <div class="abs mode-btn mode-auto">Automatic</div>

  <div class="abs panel info-panel"></div>
  <div class="abs status-banner">RUNNING ONLINE</div>

  <div class="abs readout" style="top:806px">83 °C</div>
  <div class="abs readout-label" style="top:812px">WATER<br>TEMP</div>
  <div class="abs readout" style="top:906px">3.8 BAR</div>
  <div class="abs readout-label" style="top:910px">OIL<br>PRESSURE</div>
  <div class="abs readout" style="top:994px">1500</div>
  <div class="abs readout-label" style="top:1018px">RPM</div>
  <div class="abs readout" style="top:1091px">0h 0m 0s</div>
  <div class="abs readout-label" style="top:1095px">ONLINE<br>TIME</div>

  <div class="abs electrical">
    230 VAC<br>400 VAC<br>50.0 Hz
    <div class="gap"></div>
    0 A L1<br>0 A L2<br>0 A L3
    <div class="gap"></div>
    0 KVA<br>0.00 PF
  </div>

  <div class="abs panel power-panel"></div>
  <div class="abs load-pct">63 <small>%</small></div>
  <div class="abs scale-label" style="top:366px">100</div>
  <div class="abs scale-label" style="top:706px">50</div>
  <div class="abs scale-label" style="top:1052px">0</div>
  <div class="abs tick" style="top:378px"></div>
  <div class="abs tick" style="top:720px"></div>
  <div class="abs tick" style="top:1064px"></div>
  <div class="abs tube" role="img" aria-label="Generator load bar graph at 63 percent">
    <div class="seg"></div><div class="seg"></div><div class="seg"></div><div class="seg"></div>
    <div class="seg"></div><div class="seg"></div><div class="seg"></div><div class="seg"></div>
    <div class="seg"></div><div class="seg on"></div><div class="seg on"></div><div class="seg on"></div>
    <div class="seg on"></div><div class="seg on"></div><div class="seg on"></div><div class="seg on"></div>
    <div class="seg on"></div><div class="seg on"></div><div class="seg on"></div><div class="seg on"></div>
    <div class="seg on"></div><div class="seg on"></div><div class="seg on"></div><div class="seg on"></div>
    <div class="seg on"></div>
  </div>
  <div class="abs kw-value">41</div>
  <div class="abs kw-unit">KW</div>
</body>
</html>
```